KAVLO ZenOS app needs a fun consumer interface design

KAVLO is a file transfer app aimed at consumers to help them get files onto their ZenOS devices. The app is based around each user having a personalised upload web address, and the ability to issue temporary time limited upload codes to friends and colleagues that they can use to send them files. The first version is already live in the widget shelf but we are working on a second, simplified version. You can see the screen shots for this on www.kavlo-example.com and I have attached a quick guide to app flow. The app now looks like a standard templated ZenOS 7 app. We need a design for the app that give it its own look, whilst retaining the standard ZenOS cues. It needs to look good on Palmo and Slabbo. We have a far east techno feel to the app at the moment with our characters, and we want to keep the logo. The website is currently a simple template, there's an ongoing competition to redesign that too - http://jobs.pitchmarket-example.com/job.aspx?id=813964
We have a working app with a reasonable design - we are looking for someone to take that design, add the polish a professional designer can bring, to make it pixel perfect and stand out as an app that has great design as well as great functionality.
We are also looking for something that works well on Palmo and Slabbo. See the attached screenshots of the Slabbo version - we want that version to look beautiful, not the big empty screen it is now.
Updates
Thanks for the designs so far, they look good. Could you draw them up for Slabbo size screens too please. The signup/login page and new code pages I think need the most attention as each page doesn't collect that much information, and so a lot of the screen is currently blank. I think we need some sort of background to set the content into for these pages.
(file 4 and file 6 are Slabbo screenshots)
The old app is installable for free from the Widget Shelf if that helps you get a feel for it on the Slabbo.
Target Market(s)
Consumers, techno savvy
Industry/Entity Type
Store
Font styles to use
Look and feel
Each slider illustrates characteristics of the customer's brand and the style your logo design should communicate.

```html
<!DOCTYPE html>
<html lang="en">
<head>
<meta charset="utf-8">
<title>KAVLO – Login</title>
<link rel="stylesheet" href="https://fonts.googleapis.com/css2?family=Open+Sans:wght@300;400;600;700&display=swap">
<style>
  :root {
    --sky: #1b8fdc;
    --sky-deep: #1677c2;
    --sky-soft: #5fb0e8;
    --white: #ffffff;
    --field-line: #c9d9e6;
    --placeholder: #6d6d6d;
    --dots: #333333;
    --login: #fbb53b;
    --band-1: #c2477a;
    --band-2: #ee4a6b;
    --band-3: #f47c3b;
    --band-4: #f9b64a;
    --band-5: #5ec4c4;
    --band-6: #48aba6;
    --band-7: #9bcd4a;
    --band-8: #d7e98c;
  }
  html, body {
    margin: 0;
    padding: 0;
    width: 1200px;
    height: 2292px;
    overflow: hidden;
    background: var(--sky);
  }
  .screen {
    position: relative;
    width: 1200px;
    height: 2292px;
    background: var(--sky);
    font-family: "Open Sans", Arial, sans-serif;
    color: var(--white);
    overflow: hidden;
  }
  .status-bar {
    position: absolute;
    top: 0; left: 0; right: 0;
    height: 90px;
    display: flex;
    align-items: center;
    justify-content: space-between;
    padding: 0 34px;
    box-sizing: border-box;
    font-size: 40px;
    font-weight: 400;
  }
  .status-left, .status-right {
    display: flex;
    align-items: center;
    gap: 16px;
    width: 420px;
  }
  .status-right { justify-content: flex-end; }
  .status-time { font-weight: 600; }
  .brand {
    position: absolute;
    top: 240px;
    left: 0; right: 0;
    text-align: center;
  }
  .brand-name {
    font-family: "Open Sans", Arial, sans-serif;
    font-weight: 300;
    font-size: 120px;
    letter-spacing: 12px;
    color: var(--white);
    line-height: 1;
  }
  .login-form {
    position: absolute;
    left: 65px;
    right: 65px;
    top: 484px;
    margin: 0;
  }
  .field {
    height: 168px;
    background: var(--white);
    color: var(--placeholder);
    display: flex;
    align-items: center;
    justify-content: center;
    font-size: 50px;
  }
  .field + .field { border-top: 3px solid var(--field-line); }
  .field-password {
    letter-spacing: 8px;
    color: var(--dots);
    font-size: 46px;
  }
  .login-button {
    margin-top: 48px;
    height: 166px;
    background: var(--login);
    display: flex;
    align-items: center;
    justify-content: center;
    font-size: 58px;
    font-weight: 600;
    color: var(--white);
  }
  .hero-photo {
    position: absolute;
    left: 0; right: 0;
    top: 1110px;
    height: 1087px;
    background:
      radial-gradient(ellipse 45% 50% at 48% 55%, rgba(255,255,255,0.22), rgba(255,255,255,0) 70%),
      linear-gradient(180deg, var(--sky) 0%, var(--sky-soft) 35%, var(--sky-deep) 100%);
  }
  .color-band {
    position: absolute;
    left: 0; right: 0; bottom: 0;
    height: 95px;
    display: flex;
  }
  .color-band span { flex: 1; }
  .color-band span:nth-child(1) { background: var(--band-1); }
  .color-band span:nth-child(2) { background: var(--band-2); }
  .color-band span:nth-child(3) { background: var(--band-3); }
  .color-band span:nth-child(4) { background: var(--band-4); }
  .color-band span:nth-child(5) { background: var(--band-5); }
  .color-band span:nth-child(6) { background: var(--band-6); }
  .color-band span:nth-child(7) { background: var(--band-7); }
  .color-band span:nth-child(8) { background: var(--band-8); }
</style>
</head>
<body>
<main class="screen">
  <header class="status-bar">
    <div class="status-left">
      <svg class="signal" width="120" height="24" viewBox="0 0 120 24" aria-hidden="true">
        <circle cx="12" cy="12" r="9" fill="#fff"/>
        <circle cx="36" cy="12" r="9" fill="#fff"/>
        <circle cx="60" cy="12" r="9" fill="#fff"/>
        <circle cx="84" cy="12" r="8" fill="none" stroke="#fff" stroke-width="2"/>
        <circle cx="108" cy="12" r="8" fill="none" stroke="#fff" stroke-width="2"/>
      </svg>
      <span class="carrier">Telvano</span>
      <svg class="wifi" width="46" height="34" viewBox="0 0 46 34" aria-hidden="true">
        <path d="M3 11 A28 28 0 0 1 43 11" fill="none" stroke="#fff" stroke-width="5" stroke-linecap="round"/>
        <path d="M10 19 A18 18 0 0 1 36 19" fill="none" stroke="#fff" stroke-width="5" stroke-linecap="round"/>
        <circle cx="23" cy="29" r="4.5" fill="#fff"/>
      </svg>
    </div>
    <span class="status-time">4:21 PM</span>
    <div class="status-right">
      <span class="battery-level">100%</span>
      <svg class="battery" width="80" height="34" viewBox="0 0 80 34" aria-hidden="true">
        <rect x="2" y="2" width="68" height="30" rx="5" fill="none" stroke="#fff" stroke-width="3"/>
        <rect x="7" y="7" width="58" height="20" rx="2" fill="#fff"/>
        <rect x="72" y="11" width="5" height="12" rx="2" fill="#fff"/>
      </svg>
    </div>
  </header>

  <div class="brand">
    <span class="brand-name">KAVLO</span>
  </div>

  <form class="login-form">
    <div class="field field-username">Username</div>
    <div class="field field-password">●●●●●●●●●●</div>
    <div class="login-button">Login</div>
  </form>

  <div class="hero-photo" role="img" aria-label="Blue-tinted photo of a smiling woman looking at her phone in front of city buildings"></div>

  <div class="color-band" aria-hidden="true">
    <span></span><span></span><span></span><span></span>
    <span></span><span></span><span></span><span></span>
  </div>
</main>
</body>
</html>
```